Management Consultancy needs sharp professional services showcased in a brochure

We are a management consultancy specializing on contract management and conflict avoidance services requiring a professional brochure showcasing our services to prospective clients.

Attached are a selection of existing stationary and the colour scheme.

Further details on our company can be found at www.velto-advisory-partners.com
Updates

Preference is for bi-fold, however, innovative tri-fold will be considered. Added Monday, August 7, 2017

Target Market(s)

Construction companies, consultants, developers, oil and gas service providers, NGO's, SME's.

Industry/Entity Type

Management

Requirements
Must have
• High degree of professionalism with eye catching, sharp detail. No frils.
• Colour scheme as per the attachments
• Font as per attachments - Century Gothic
• Details of our company and services
Nice to have
• Open to ideas, thinking along the lines of a car brochure type design.
• Bi-fold preferred, by trifold accepted if innovative.
Should not have
• Remove reference to the United Arab Emirates.
• No cartoon/clipart photos.

```html
<!DOCTYPE html>
<html lang="en">
<head>
<meta charset="utf-8">
<title>Velto Advisory – Bi-fold Brochure</title>
<link href="https://fonts.googleapis.com/css2?family=Questrial&family=Cinzel:wght@500&display=swap" rel="stylesheet">
<style>
  :root {
    --navy: #2c3d5e;
    --navy-deep: #243452;
    --red: #a8202c;
    --paper: #f3f4f7;
    --paper-shade: #e2e4ea;
    --ink: #2c3d5e;
    --white: #ffffff;
    --stage: #3a3a3c;
    --photo-a: #c9ccd4;
    --photo-b: #8a8f9c;
  }
  * { box-sizing: border-box; margin: 0; padding: 0; }
  html, body { width: 1200px; height: 789px; overflow: hidden; background: var(--stage); }
  body { font-family: "Questrial", "Century Gothic", sans-serif; }
  .spread {
    position: absolute; left: 80px; top: 27px;
    width: 1040px; height: 735px; display: flex;
    box-shadow: 0 10px 30px rgba(0,0,0,.45);
  }
  .page { position: relative; width: 520px; height: 735px; overflow: hidden; }
  .page--back { background: var(--navy); color: var(--white); }
  .page--front { background: var(--paper); }
  .page svg.art { position: absolute; inset: 0; }

  .about { position: absolute; left: 44px; top: 62px; width: 330px; }
  .about__title { font-size: 22px; letter-spacing: 1px; font-weight: 700; }
  .about__title span { font-weight: 400; }
  .about__rule { height: 1px; background: rgba(255,255,255,.6); margin: 8px 0 10px; width: 320px; }
  .about__lead { font-size: 11px; line-height: 1.35; color: #dfe3ec; }
  .about__list { list-style: none; margin-top: 6px; font-size: 10.5px; font-weight: 700; line-height: 1.45; }
  .about__list li::before { content: "▲"; font-size: 8px; margin-right: 8px; color: #dfe3ec; }

  .brand { font-family: "Cinzel", "Century Gothic", serif; font-weight: 500; letter-spacing: 1px; display: flex; align-items: center; gap: 10px; }
  .brand__dot { width: 14px; height: 14px; border-radius: 50%; }
  .page--back .brand { position: absolute; left: 44px; top: 612px; font-size: 28px; color: var(--white); }
  .page--back .brand__dot { background: var(--white); }

  .contact { position: absolute; left: 44px; top: 660px; font-size: 12px; line-height: 1.7; color: #dfe3ec; list-style: none; }
  .contact b { color: var(--white); font-weight: 400; }
  .contact svg { vertical-align: -2px; margin-right: 8px; }

  .headline { position: absolute; left: 40px; top: 560px; line-height: 1.15; }
  .headline__top { font-size: 21px; color: var(--red); letter-spacing: .5px; }
  .headline__bottom { font-size: 16px; color: var(--ink); font-weight: 700; letter-spacing: 1px; }
  .page--front .brand { position: absolute; right: 30px; top: 566px; font-size: 26px; color: var(--ink); }
  .page--front .brand__dot { background: var(--ink); }
  .front-url { position: absolute; left: 40px; top: 622px; font-size: 11px; color: var(--ink); }
  .front-url b { color: var(--red); font-weight: 400; }
  .front-rule { position: absolute; left: 40px; right: 30px; top: 648px; height: 2px; background: var(--red); }
</style>
</head>
<body>
<main class="spread">
  <section class="page page--back">
    <svg class="art" width="520" height="735" viewBox="0 0 520 735">
      <defs>
        <linearGradient id="photoTeam" x1="0" y1="0" x2="1" y2="1">
          <stop offset="0" stop-color="var(--photo-a)"/>
          <stop offset="1" stop-color="var(--photo-b)"/>
        </linearGradient>
      </defs>
      <path d="M430 0 Q520 40 520 0 Z" fill="var(--navy-deep)"/>
      <path d="M380 0 C420 80 440 160 520 230 L520 0 Z" fill="#d9dbe2"/>
      <path d="M380 0 C420 80 440 160 520 230 L520 250 C430 170 400 90 360 0 Z" fill="var(--red)"/>
      <circle cx="250" cy="390" r="180" fill="var(--red)"/>
      <circle cx="254" cy="384" r="172" fill="var(--white)"/>
      <circle cx="254" cy="384" r="166" fill="url(#photoTeam)" role="img" aria-label="Photo: two consultants in shirts and ties reviewing work on a laptop"/>
    </svg>

    <div class="about">
      <h2 class="about__title">ABOUT <span>US</span></h2>
      <div class="about__rule"></div>
      <p class="about__lead">We are an experienced contract and conflict advisory providing global contract performance solutions and conflict management to:</p>
      <ul class="about__list">
        <li>International Development Organisations;</li>
        <li>Construction Industry;</li>
        <li>Oil And Gas Industry; And</li>
        <li>Government Sectors.</li>
      </ul>
    </div>

    <div class="brand"><span class="brand__dot"></span>Velto Advisory</div>

    <ul class="contact">
      <li><svg width="12" height="9" viewBox="0 0 12 9"><rect x=".5" y=".5" width="11" height="8" fill="none" stroke="#fff"/><path d="M.5 .5 6 5 11.5 .5" fill="none" stroke="#fff"/></svg>mhale@<b>velto-advisory-partners</b>.com</li>
      <li><svg width="11" height="11" viewBox="0 0 11 11"><circle cx="5.5" cy="5.5" r="5" fill="none" stroke="#fff"/><path d="M.5 5.5h10M5.5 .5c-3 3-3 7 0 10M5.5 .5c3 3 3 7 0 10" fill="none" stroke="#fff"/></svg>www.<b>velto-advisory-partners</b>.com</li>
    </ul>
  </section>

  <section class="page page--front">
    <svg class="art" width="520" height="735" viewBox="0 0 520 735">
      <defs>
        <linearGradient id="photoMeeting" x1="0" y1="0" x2="1" y2="1">
          <stop offset="0" stop-color="#e6e8ee"/>
          <stop offset=".55" stop-color="#9aa0ad"/>
          <stop offset="1" stop-color="#5a4a44"/>
        </linearGradient>
      </defs>
      <path d="M420 0 L520 0 L520 60 Z" fill="var(--navy)"/>
      <path d="M0 0 L0 420 C0 480 60 530 170 540 C320 552 470 470 520 380 L520 0 Z" fill="var(--red)"/>
      <path d="M0 0 L0 405 C10 460 70 510 170 520 C320 532 460 455 520 360 L520 0 Z" fill="url(#photoMeeting)" role="img" aria-label="Photo: smiling businessman and businesswoman reviewing a tablet together"/>
      <path d="M0 0 C40 60 20 130 0 180 Z" fill="var(--navy)"/>
      <path d="M330 560 C420 520 480 480 520 440 L520 470 C480 510 420 545 340 575 Z" fill="var(--paper-shade)"/>
    </svg>

    <div class="headline">
      <p class="headline__top">THE CONTRACT AND</p>
      <p class="headline__bottom">CONFLICT ADVISORY</p>
    </div>
    <div class="brand"><span class="brand__dot"></span>Velto Advisory</div>
    <p class="front-url">www.<b>velto-advisory-partners</b>.com</p>
    <div class="front-rule"></div>
  </section>
</main>
</body>
</html>
```